Business Card design for shipping company 'FERNHOLT INTERNATIONAL LTD'

Classic / traditional business card in black Garamond / Times New Roman or similar text for a shipping / marine transport company, containing the following information:

QUOTE

FERNHOLT INTERNATIONAL LTD

MARTIN QUESTEDGE FICS

T: +44 7902 615370
E: cargo@fernholt-example.com

UNQUOTE

Target Market(s)

Marine / Shipping industry

Contact Information for Business Card

FERNHOLT INTERNATIONAL LTD MARTIN QUESTEDGE FICS T: +44 7902 615370 E: cargo@fernholt-example.com

Font styles to use
Serif

Colors

Designer to choose colors to be used in the design.

Requirements
Must have
• Garamond / Times New Roman or similar text in black colour

```html
<!DOCTYPE html>
<html lang="en">
<head>
<meta charset="utf-8">
<title>Fernholt International Ltd — Business Card</title>
<link href="https://fonts.googleapis.com/css2?family=Tinos:wght@400;700&display=swap" rel="stylesheet">
<style>
  :root {
    --backdrop: #e6e6e6;
    --card: #f7f7f6;
    --ink: #1c1c1c;
    --ink-soft: #3a3a3a;
    --rule: #2a2a2a;
  }
  * { box-sizing: border-box; margin: 0; padding: 0; }
  html, body {
    width: 1200px;
    height: 716px;
    overflow: hidden;
    background: var(--backdrop);
  }
  .stage {
    width: 1200px;
    height: 716px;
    display: flex;
    align-items: center;
    justify-content: center;
  }
  .business-card {
    position: relative;
    width: 860px;
    height: 520px;
    background: var(--card);
    box-shadow: 0 6px 18px rgba(0, 0, 0, 0.12);
    font-family: "Tinos", "Times New Roman", serif;
    color: var(--ink);
  }
  .card-frame {
    position: absolute;
    inset: 48px 52px 52px 52px;
    border: 1.5px solid var(--rule);
  }
  .company-name {
    position: absolute;
    top: 36px;
    left: 150px;
    padding: 0 16px;
    background: var(--card);
    font-weight: 700;
    font-size: 21px;
    letter-spacing: 1.2px;
    line-height: 24px;
    color: var(--ink);
  }
  .person {
    position: absolute;
    top: 218px;
    left: 200px;
    white-space: nowrap;
  }
  .person-name {
    font-weight: 700;
    font-size: 46px;
    letter-spacing: 2px;
    color: var(--ink);
  }
  .person-credential {
    font-size: 17px;
    letter-spacing: 2px;
    vertical-align: 22px;
    margin-left: 8px;
    color: var(--ink-soft);
  }
  .contact {
    position: absolute;
    top: 330px;
    left: 0;
    right: 0;
    text-align: center;
    font-size: 24px;
    line-height: 30px;
    color: var(--ink-soft);
    list-style: none;
  }
</style>
</head>
<body>
  <main class="stage">
    <article class="business-card">
      <div class="card-frame"></div>
      <p class="company-name">FERNHOLT INTERNATIONAL LTD</p>
      <h1 class="person">
        <span class="person-name">MARTIN QUESTEDGE</span><span class="person-credential">FICS</span>
      </h1>
      <ul class="contact">
        <li class="contact-phone">+44 7902 615370</li>
        <li class="contact-email">cargo@fernholt-example.com</li>
      </ul>
    </article>
  </main>
</body>
</html>
```